Engineering Consultant Business Card

I'm starting a new business as a high-end engineering consultant in a niche field. I've attached the jpg for my logo plus the branding guideline document that I've been following. You can see my business website here: www.tarvikworks.com
I'd like a business card that has the logo on one side, then the other side has (in any order): Tarvik Works, Inc.
Dana Whitlock
President and Chief EMC Engineer
www.tarvikworks.com
dana@tarvikworks.com
Optional: motto "We will solve your EMC problems as early as possible—ideally before they even start."
I'm not planning on including a phone number
Target Market(s)
Businesses, especially makers of electronics hardware
Industry/Entity Type
Electrical engineering
Contact Information for Business Card
Company name, my name, website, email

```html
<!DOCTYPE html>
<html lang="en">
<head>
<meta charset="UTF-8">
<title>Tarvik Works, Inc. — Business Card</title>
<link href="https://fonts.googleapis.com/css2?family=Open+Sans:wght@400;700&display=swap" rel="stylesheet">
<style>
  :root {
    --backdrop: #d6d6d6;
    --paper: #f1f1f2;
    --brand-blue: #0f2a9c;
    --ink: #111111;
    --band-text: #e6e9f7;
  }
  * { margin: 0; padding: 0; box-sizing: border-box; }
  html, body {
    width: 1200px; height: 1051px; overflow: hidden;
    background: var(--backdrop);
    font-family: "Open Sans", Arial, sans-serif;
  }
  .card-set {
    position: absolute; left: 50px; top: 370px;
    display: flex; gap: 40px;
  }
  .card {
    position: relative; width: 530px; height: 310px;
    background: var(--paper);
    box-shadow: 0 14px 30px rgba(0,0,0,0.18);
    overflow: hidden;
  }
  /* Contact side */
  .identity {
    position: absolute; right: 285px; top: 110px; text-align: right;
  }
  .identity__name {
    color: var(--brand-blue); font-weight: 700; font-size: 22px; line-height: 1.1;
  }
  .identity__title {
    color: var(--ink); font-size: 13.5px; margin-top: 2px;
  }
  .divider {
    position: absolute; left: 262px; top: 70px; width: 1px; height: 150px;
    background: var(--brand-blue);
  }
  .contacts {
    position: absolute; left: 282px; top: 122px; list-style: none;
    font-size: 15px; color: var(--ink);
  }
  .contacts li { display: flex; align-items: center; gap: 7px; line-height: 1.35; }
  .contacts svg { width: 12px; height: 12px; flex: none; }
  .motto-band {
    position: absolute; left: 0; right: 0; bottom: 24px; height: 22px;
    background: var(--brand-blue); color: var(--band-text);
    font-size: 11.5px; line-height: 22px; padding-left: 24px;
  }
  /* Brand side */
  .card--brand { border-bottom: 8px solid var(--brand-blue); }
  .brand-mark {
    position: absolute; inset: 0;
    display: flex; align-items: center; justify-content: center; gap: 16px;
  }
  .brand-mark__dot {
    width: 40px; height: 40px; border-radius: 50%; background: var(--brand-blue);
  }
  .brand-mark__name {
    color: var(--brand-blue); font-weight: 700; font-size: 44px; letter-spacing: 0.5px;
  }
</style>
</head>
<body>
  <main class="card-set">
    <section class="card card--contact" aria-label="Contact side">
      <div class="identity">
        <p class="identity__name">Dana Whitlock</p>
        <p class="identity__title">President and Chief EMC Engineer</p>
      </div>
      <div class="divider"></div>
      <ul class="contacts">
        <li>
          <svg viewBox="0 0 12 12" aria-hidden="true"><circle cx="6" cy="6" r="5.5" fill="var(--brand-blue)"/><path d="M1 6h10M6 .5c-2.5 3-2.5 8 0 11M6 .5c2.5 3 2.5 8 0 11" stroke="#fff" stroke-width="0.8" fill="none"/></svg>
          www.tarvikworks.com
        </li>
        <li>
          <svg viewBox="0 0 12 12" aria-hidden="true"><rect x="0.5" y="2.5" width="11" height="8" fill="var(--brand-blue)"/><path d="M0.5 2.5L6 7l5.5-4.5" stroke="#fff" stroke-width="0.9" fill="none"/></svg>
          dana@tarvikworks.com
        </li>
      </ul>
      <p class="motto-band">We will solve your EMC problems as early as possible—ideally before they even start.</p>
    </section>

    <section class="card card--brand" aria-label="Brand side">
      <div class="brand-mark">
        <span class="brand-mark__dot"></span>
        <span class="brand-mark__name">Tarvik Works</span>
      </div>
    </section>
  </main>
</body>
</html>
```